We need a book cover design for a handbook related to the implementation of new European privacy regulation. The topic is quite technical but the goal is to have something actionnable for small businesses and small non-profit organizations. It's really a handbook that should inspire confidence for the managers who have to be compliant in a pragmatic way (not like big corporate structures). The final format should be in PDF with specific requirements to be publish on PrintHollow.com.

Title: KVRT Guidebook for local traders
Subtitle: Be ready in 21 days (or less)
Author: Marcel Vendrione
Edition: 1.0
ISBN-13: 978-1574203658
ISBN-10: 1574203652

The book has a size of 6" x 9" and is composed by 52 pages.
Spine width should be 52 x 0.002252 = 0,117104"
Additional technical info in the attachments.

For text and inspiration about the covers (rear cover especially), please use the text on https://www.kvrt-guidebook.eu.

Feel free to ask questions to clarify some aspects!

Target Market(s)

Managing Directors of small businesses

Industry/Entity Type

Technical

Colors

Designer to choose colors to be used in the design.

Requirements
Must have
• - Inspire confidence and accessibility (simple, easy, time effective)
• - Title, subtitle and author on the front cover
• - ISBNs, barcode and mention "Templates available on https://www.kvrt-guidebook.eu" + text coming from the website
Nice to have
• - Simplicity
• - Easy path to compliance, shortcut
• - Time saving
Should not have
• - Picture of the author
• - Text on the spine

```html
<!DOCTYPE html>
<html lang="en">
<head>
<meta charset="utf-8">
<title>KVRT Guidebook for local traders – Cover options</title>
<link rel="stylesheet" href="https://fonts.googleapis.com/css2?family=Roboto+Slab:wght@800;900&family=Open+Sans:wght@400;700&family=Cinzel:wght@600&family=Gochi+Hand&display=swap">
<style>
  :root {
    --stage-top: #cfd0d2;
    --stage-bottom: #f4f4f4;
    --label-grey: #5e5e5e;
    --b-top: #1f5d8c;
    --b-bottom: #0d2450;
    --b-map: #123a6a;
    --accent-yellow: #f3c532;
    --band-yellow: #f7d43a;
    --ink-dark: #1c1c2e;
    --white: #ffffff;
    --a-base: #3d3f9f;
    --a-light: #5557b8;
    --a-header: #24246f;
  }
  * { box-sizing: border-box; margin: 0; padding: 0; }
  html, body { width: 1200px; height: 819px; overflow: hidden; }
  body {
    position: relative;
    background: linear-gradient(180deg, var(--stage-top) 0%, var(--stage-bottom) 70%);
    font-family: "Open Sans", Arial, sans-serif;
  }

  .cover {
    position: absolute;
    width: 360px;
    height: 540px;
    overflow: hidden;
    box-shadow: 0 10px 24px rgba(0, 0, 0, 0.25);
  }
  .option-label {
    position: absolute;
    width: 360px;
    text-align: center;
    font-family: "Open Sans", Arial, sans-serif;
    font-weight: 700;
    font-size: 26px;
    letter-spacing: 1px;
    color: var(--label-grey);
  }

  .title-main, .title-sub {
    font-family: "Roboto Slab", Georgia, serif;
    font-weight: 900;
    line-height: 1;
    text-transform: uppercase;
  }
  .title-tag {
    font-family: "Open Sans", Arial, sans-serif;
    line-height: 1;
  }
  .subtitle-band {
    position: absolute;
    font-family: "Gochi Hand", cursive;
    color: var(--ink-dark);
    line-height: 1;
    white-space: nowrap;
  }
  .author {
    position: absolute;
    left: 0;
    width: 100%;
    text-align: center;
    font-family: "Cinzel", Georgia, serif;
    font-weight: 600;
    color: var(--white);
    letter-spacing: 1px;
  }

  /* Option B */
  .cover-b {
    left: 185px; top: 140px;
    background: linear-gradient(180deg, var(--b-top) 0%, var(--b-bottom) 45%, var(--b-bottom) 100%);
  }
  .cover-b .title-block { position: absolute; left: 96px; top: 34px; right: 0; }
  .cover-b .title-main { font-size: 58px; color: var(--accent-yellow); }
  .cover-b .title-sub { font-size: 27px; color: var(--accent-yellow); margin-top: 6px; letter-spacing: 1px; }
  .cover-b .title-rule { height: 2px; background: var(--accent-yellow); margin-top: 4px; }
  .cover-b .title-tag { font-size: 21px; color: var(--white); margin-top: 8px; }
  .cover-b .emblem-art {
    position: absolute; left: 40px; top: 235px; width: 270px; height: 170px;
    background: radial-gradient(ellipse at 55% 50%, var(--b-map) 0%, rgba(18, 58, 106, 0.4) 55%, rgba(13, 36, 80, 0) 80%);
  }
  .cover-b .subtitle-band {
    left: 72px; top: 398px; width: 262px; height: 26px;
    background: var(--band-yellow);
    transform: rotate(-4deg);
    font-size: 18px; text-align: center; padding-top: 3px;
  }
  .cover-b .author { top: 468px; font-size: 18px; }

  /* Option A */
  .cover-a {
    left: 650px; top: 130px;
    background: linear-gradient(180deg, var(--a-base) 0%, var(--a-base) 60%, var(--a-light) 100%);
  }
  .cover-a .header-panel {
    position: absolute; left: 42px; top: 0; width: 318px; height: 158px;
    background: var(--a-header);
    border-bottom-left-radius: 22px;
  }
  .cover-a .title-block { position: absolute; left: 66px; top: 26px; right: 14px; text-align: right; }
  .cover-a .title-main { font-size: 60px; color: var(--white); padding-right: 24px; }
  .cover-a .title-sub { font-size: 31px; color: var(--white); margin-top: 2px; }
  .cover-a .title-tag { font-size: 24px; color: var(--accent-yellow); margin-top: 8px; }
  .cover-a .subtitle-band {
    left: 102px; top: 160px; width: 258px; height: 30px;
    background: var(--band-yellow);
    font-size: 18px; padding: 5px 0 0 10px;
  }
  .cover-a .wave-art {
    position: absolute; left: 0; top: 200px; width: 360px; height: 290px;
    background: linear-gradient(160deg, rgba(255, 255, 255, 0) 20%, rgba(190, 192, 240, 0.22) 50%, rgba(255, 255, 255, 0) 80%);
  }
  .cover-a .author { top: 460px; font-size: 17px; }
</style>
</head>
<body>
  <section class="cover cover-b" aria-label="Cover option B">
    <div class="title-block">
      <div class="title-main">KVRT</div>
      <div class="title-sub">Guidebook</div>
      <div class="title-rule"></div>
      <div class="title-tag">for local traders</div>
    </div>
    <div class="emblem-art" role="img" aria-label="Dotted map of Europe with a ring of yellow stars around a white padlock"></div>
    <div class="subtitle-band">Be ready in 21 days (or less)</div>
    <div class="author">Marcel Vendrione</div>
  </section>
  <div class="option-label" style="left:185px; top:696px;">OPTION - B</div>

  <section class="cover cover-a" aria-label="Cover option A">
    <div class="header-panel"></div>
    <div class="title-block">
      <div class="title-main">KVRT</div>
      <div class="title-sub">Guidebook</div>
      <div class="title-tag">for local traders</div>
    </div>
    <div class="subtitle-band">Be ready in 21 days (or less)</div>
    <div class="wave-art" role="img" aria-label="Flowing mesh of fine light wave lines across the cover"></div>
    <div class="author">Marcel Vendrione</div>
  </section>
  <div class="option-label" style="left:650px; top:692px;">OPTION - A</div>
</body>
</html>
```